Spray Foam Company Business Card

We need a business card designed for our spray foam insulation and roof coatings business. We handle residential and commercial projects.
Construction
We would like it to say:
R & K Spray
with these bullet points
-foam insulation
-waterproofing roof system
-water proofing foundation systems
website is rksprayfoaminsulation.example (this was just purchased)
office phone : 630-482-9164
And 3 cards with names on them the names are :
Derek Halvorsen
Curtis Pennington
Rob Stallworth
maybe the bullet points can go on the back?
if you go this website it is another division of our company and you can see the font we use in the R & K. We do not want to use the same half circles that it has just the lettering
www.coatedrightforyears.example

```html
<!DOCTYPE html>
<html lang="en">
<head>
<meta charset="utf-8">
<title>R &amp; K Spray – Business Card</title>
<link rel="stylesheet" href="https://fonts.googleapis.com/css2?family=Crimson+Pro:ital,wght@1,600&family=Open+Sans:wght@400;600;700&display=swap">
<style>
  :root {
    --page-bg: #ece9e6;
    --card-bg: #ffffff;
    --navy: #3b2f86;
    --sky: #4ea3dd;
    --ink: #3a3a3a;
    --strip-top: #3b2f86;
    --strip-bottom: #4ea6e0;
  }
  * { margin: 0; padding: 0; box-sizing: border-box; }
  html, body {
    width: 1200px; height: 406px; overflow: hidden;
    background: var(--page-bg);
  }
  .canvas { position: relative; width: 1200px; height: 406px; }
  .card {
    position: absolute; top: 70px;
    width: 468px; height: 266px;
    background: var(--card-bg);
    box-shadow: 0 2px 6px rgba(0,0,0,0.18);
    overflow: hidden;
  }
  .card--front { left: 122px; }
  .card--back { left: 610px; }
  .card__strip {
    position: absolute; left: 0; top: 0;
    width: 40px; height: 100%;
    background: linear-gradient(to bottom, var(--strip-top), var(--strip-bottom));
  }
  .card__rule {
    position: absolute; left: 42px; top: 0;
    width: 2px; height: 100%;
    background: linear-gradient(to bottom, var(--strip-top), var(--strip-bottom));
  }
  .brand {
    position: absolute; left: 104px; top: 34px;
    font-family: "Open Sans", sans-serif;
    font-weight: 600; font-size: 30px;
    color: var(--navy); letter-spacing: 1px;
  }
  .holder-name {
    position: absolute; left: 104px; top: 100px;
    font-family: "Crimson Pro", serif;
    font-style: italic; font-weight: 600; font-size: 23px;
    color: var(--ink);
  }
  .name-frame { position: absolute; left: 0; top: 0; }
  .contact {
    position: absolute; left: 104px;
    font-family: "Open Sans", sans-serif;
    font-size: 11.5px; line-height: 16px; color: var(--ink);
  }
  .contact--postal { top: 162px; }
  .contact--online { top: 205px; font-weight: 700; }
  .services {
    position: absolute; left: 86px; top: 180px;
    list-style: none;
    font-family: "Open Sans", sans-serif;
    font-weight: 700; font-size: 11.5px; line-height: 16.5px;
    color: var(--ink);
  }
  .services li::before {
    content: ""; display: inline-block;
    width: 4px; height: 4px; border-radius: 50%;
    background: var(--sky);
    margin-right: 5px; vertical-align: middle;
    position: relative; top: -1px;
  }
</style>
</head>
<body>
<main class="canvas">
  <section class="card card--front">
    <div class="card__strip"></div>
    <div class="card__rule"></div>
    <div class="brand">R &amp; K</div>
    <div class="holder-name">Derek Halvorsen</div>
    <svg class="name-frame" width="468" height="266" viewBox="0 0 468 266" aria-hidden="true">
      <path d="M254 112 H436 Q446 112 446 122 V235 Q446 245 436 245 H66"
            fill="none" stroke="var(--navy)" stroke-width="1.4"/>
    </svg>
    <p class="contact contact--postal">218 Millstone Lane, Yorkville, IL 60560<br>Phone : 630-482-9164</p>
    <p class="contact contact--online">Email : info@coatedrightforyears.example<br>Website : rksprayfoaminsulation.example</p>
  </section>

  <section class="card card--back">
    <div class="card__strip"></div>
    <div class="card__rule"></div>
    <div class="brand">R &amp; K</div>
    <ul class="services">
      <li>foam insulation</li>
      <li>waterproofing roof system</li>
      <li>water proofing foundation systems</li>
    </ul>
  </section>
</main>
</body>
</html>
```